design a company brochure

tri-fold brochure. reference website: orvan.llc for information (website under construction but should have the basic information)

Target Market(s)

Users of sign Language interpreting services; businesses, community, hospitals, schools, colleges, medical, religious, and legal settings

Industry/Entity Type

Community Service

Font styles to use
Serif
Decorative

Colors
734ea0
9ccb3b

Requirements
Must have
• Brochure should be worded so it applies to the above markets and focuses on our professionalism, integrity in business
Nice to have
• I would like the designers to look at the business website under construction (orvan.llc) or an older website (orvan-tdku.com). Company was restructured and is now just ORVAN, LLC.
A darker green than what is shown here. Again, reference the website
Should not have
• No personal pictures in the brochure - can use clip art or interpreter/interpreting shots.

```html
<!DOCTYPE html>
<html lang="en">
<head>
<meta charset="utf-8">
<title>ORVAN, LLC – Tri-fold Brochure</title>
<link href="https://fonts.googleapis.com/css2?family=Libre+Baskerville:wght@400;700&family=Montserrat:wght@200;300;400;600;700;800&display=swap" rel="stylesheet">
<style>
:root{
  --purple:#734ea0;
  --purple-deep:#5f3d8c;
  --green:#9ccb3b;
  --ink:#3a3a3a;
  --muted:#666;
  --paper:#ffffff;
  --page-bg:#ffffff;
}
*{box-sizing:border-box;margin:0;padding:0}
html,body{width:1200px;height:4000px;overflow:hidden;background:var(--page-bg)}
body{font-family:'Montserrat',Arial,sans-serif;color:var(--ink)}
.sheet{position:absolute;left:50px;width:1100px;height:770px;display:flex;background:var(--paper);box-shadow:0 6px 22px rgba(0,0,0,.25)}
.sheet--outside{top:1160px}
.sheet--inside{top:2050px}
.panel{position:relative;width:367px;height:100%;overflow:hidden}
.panel--purple{background:linear-gradient(180deg,var(--purple) 0%,var(--purple-deep) 100%);color:#fff}
.sheet::after{content:"";position:absolute;left:0;right:0;bottom:0;height:6px;background:var(--green)}
.heading{font-family:'Libre Baskerville',Georgia,serif;font-weight:400;color:var(--purple);font-size:30px;letter-spacing:.5px;text-transform:uppercase}
.photo{display:block;border-radius:0}
.body{font-size:8.6px;line-height:1.42;color:var(--muted)}
/* about */
.about{padding:70px 30px 0 46px}
.about .heading{margin-bottom:16px}
.bio{display:flex;gap:16px}
.bio__portrait{width:124px;flex:none}
.bio__portrait .photo{width:124px;height:166px}
.bio__tag{background:var(--green);color:#fff;padding:5px 8px;font-size:10px;font-weight:700;line-height:1.2}
.bio__tag span{display:block;font-weight:400}
.bio + .bio{margin-top:34px}
.about__tail{margin-top:6px}
/* logo stand-in */
.brandmark{display:flex;align-items:center;gap:10px;font-family:'Libre Baskerville',Georgia,serif;font-weight:700;font-size:22px}
.brandmark__box{width:16px;height:16px;border:2px solid currentColor}
/* contact */
.contact{text-align:center;padding:64px 34px 0}
.contact .brandmark{justify-content:center;color:#fff}
.contact .heading{color:#fff;font-size:32px;margin:110px 0 22px}
.contact .body{color:#eee;font-size:9px}
.contact__list{margin-top:44px;font-size:14px;line-height:1.3}
.contact__list li{list-style:none;margin-bottom:16px}
.contact__list svg{display:block;margin:0 auto 6px;width:20px;height:20px}
.footer{position:absolute;left:30px;right:30px;bottom:34px;text-align:center;font-size:9px;line-height:1.4;color:#fff}
/* cover */
.cover__bar{position:absolute;right:0;width:20px;background:var(--green)}
.cover__bar--top{top:0;height:66px}
.cover__bar--bottom{top:530px;bottom:0}
.cover .brandmark{position:absolute;left:100px;top:76px;color:var(--ink)}
.cover__photo{position:absolute;left:78px;top:165px;width:289px;height:318px}
.cover__title{position:absolute;left:10px;top:700px;transform-origin:left top;transform:rotate(-90deg);white-space:nowrap;font-size:56px;line-height:1;color:#222}
.cover__title .light{font-weight:200}
.cover__title .bold{font-weight:800}
.cover__tagline{position:absolute;left:100px;top:545px;width:225px;font-size:14px;line-height:1.35;color:#333}
.cover__name{position:absolute;left:100px;top:672px;font-family:'Libre Baskerville',Georgia,serif;font-weight:700;font-size:20px;color:#222}
/* services */
.services{padding:32px 30px 0 46px}
.services .heading{margin-bottom:12px}
.services .strong{font-weight:700;color:#444;margin-top:10px}
.service-card{margin-top:22px}
.service-card .photo{width:270px;height:94px}
.service-card__label{background:var(--green);color:#fff;font-size:15px;font-weight:600;letter-spacing:1px;padding:6px 14px;width:270px;text-transform:uppercase}
.bullets{display:grid;grid-template-columns:1fr 1fr;gap:6px 14px;margin-top:14px;font-size:9px;font-weight:600;color:#444;list-style:none}
.bullets li{position:relative;padding-left:12px;line-height:1.3}
.bullets li::before{content:"";position:absolute;left:0;top:3px;width:6px;height:6px;border-radius:50%;background:var(--purple)}
.panel--purple .bullets{color:#fff}
.panel--purple .bullets li::before{background:#fff}
.settings{padding:44px 46px 0}
.settings .service-card{margin-top:0}
.settings .service-card + .bullets{margin-bottom:26px}
.settings .photo,.settings .service-card__label{width:100%}
.settings .photo{height:104px}
.settings .service-card__label{font-size:16px}
/* resources */
.resources{padding:32px 36px 0 40px}
.resources .heading{margin-bottom:18px}
.qa{display:flex;gap:10px;margin-bottom:16px}
.qa__marks{flex:none;font-family:'Libre Baskerville',Georgia,serif;font-size:13px;font-weight:700;line-height:1.25;color:var(--purple)}
.qa__marks span{display:block;color:var(--green)}
.qa__q{font-size:8.4px;font-weight:700;color:var(--green);text-transform:uppercase;line-height:1.3;margin-bottom:2px}
.qa .body{font-size:8.4px}
.resources .heading--faq{margin-top:26px}
</style>
</head>
<body>

<!-- Outside spread -->
<section class="sheet sheet--outside">
  <article class="panel about">
    <h2 class="heading">About Us</h2>
    <div class="bio">
      <div class="bio__portrait">
        <svg class="photo" viewBox="0 0 124 166" role="img" aria-label="Portrait photo of the owner"><defs><linearGradient id="p1" x1="0" y1="0" x2="0" y2="1"><stop offset="0" stop-color="#8d8a7a"/><stop offset="1" stop-color="#3f3a34"/></linearGradient></defs><rect width="124" height="166" fill="url(#p1)"/></svg>
        <div class="bio__tag">Dana Hollis<span>Owner</span></div>
      </div>
      <p class="body">Dana Hollis is a native of Iowa but has lived in Colorado long enough to call it home. She graduated in 1998 from Ridgeline Community College with an A.A.S. degree in Interpreter Preparation and has done most of her interpreting work in the educational interpreting field. She is currently enrolled in the ASL-English Interpretation BA program at Eastvale University.</p>
    </div>
    <div class="bio">
      <div class="bio__portrait">
        <svg class="photo" viewBox="0 0 124 166" role="img" aria-label="Portrait photo of the staffing coordinator"><defs><linearGradient id="p2" x1="0" y1="0" x2="0" y2="1"><stop offset="0" stop-color="#a7a59c"/><stop offset="1" stop-color="#2f2a28"/></linearGradient></defs><rect width="124" height="166" fill="url(#p2)"/></svg>
        <div class="bio__tag">Renata Voss<span>Staffing Coordinator</span></div>
      </div>
      <p class="body">Recognizing the great need for qualified interpreters in the public education system, she partnered with Renata Voss to offer school districts State Department of Education (SDE) credentialed interpreters for Deaf and Hard of Hearing students. By using credentialed interpreters, school districts are able to maintain compliance with SDE rules, as well as securing professional</p>
    </div>
    <p class="body about__tail">and highly qualified interpreters for their students. Renata Voss is the staffing coordinator of ORVAN, LLC. She grew up in California and moved to Colorado in 1996. She graduated from Ridgeline Community College in 2002 earning her A.A.S in Interpreter Preparation. She is currently attaining her B.S in Speech Language and Hearing Sciences. In her spare time, she enjoys spending time with her family and friends and volunteering at her church.</p>
  </article>

  <article class="panel panel--purple contact">
    <div class="brandmark"><span class="brandmark__box"></span>ORVAN, LLC</div>
    <h2 class="heading">Contact Us</h2>
    <p class="body">Thank you for your interest in ORVAN / TDKU. If you have any questions about our services or would like to schedule an interpreter, please contact us using the information below or fill out the Request an Interpreter form and one of our staff will contact you promptly. We are available 24 hours a day 7 days a week to assist you with your interpreting needs.</p>
    <ul class="contact__list">
      <li><svg viewBox="0 0 20 20" fill="none" stroke="#fff" stroke-width="1.4"><circle cx="10" cy="10" r="8"/><ellipse cx="10" cy="10" rx="3.5" ry="8"/><line x1="2" y1="10" x2="18" y2="10"/></svg>ORVAN / TDKU, LLC</li>
      <li><svg viewBox="0 0 20 20" fill="#fff"><rect x="5" y="2" width="10" height="6"/><rect x="2" y="8" width="16" height="7" rx="1"/><rect x="5" y="13" width="10" height="5" fill="#fff" stroke="#734ea0"/></svg>(555) 214-0187</li>
      <li><svg viewBox="0 0 20 20" fill="#fff"><path d="M5 2l3 4-2 2c1 3 3 5 6 6l2-2 4 3-2 3C9 18 2 11 2 4z"/></svg>(555) 308-4421</li>
      <li><svg viewBox="0 0 20 20" fill="#fff"><path d="M10 1a6 6 0 0 0-6 6c0 5 6 12 6 12s6-7 6-12a6 6 0 0 0-6-6zm0 8.5a2.5 2.5 0 1 1 0-5 2.5 2.5 0 0 1 0 5z"/></svg>PO BOX 480312<br>Denver, Colorado 80222</li>
    </ul>
    <p class="footer">ORVAN / TDKU, LLC &nbsp;|&nbsp; VOICE : (555) 214-0187<br>| TEXT : (555) 308-4421 &nbsp;| PO BOX 480312 |<br>DENVER, CO 80222</p>
  </article>

  <article class="panel cover">
    <span class="cover__bar cover__bar--top"></span>
    <span class="cover__bar cover__bar--bottom"></span>
    <div class="brandmark"><span class="brandmark__box"></span>ORVAN, LLC</div>
    <svg class="cover__photo" viewBox="0 0 289 318" preserveAspectRatio="none" role="img" aria-label="Photo of hands signing in front of green pine needles"><defs><linearGradient id="c1" x1="0" y1="0" x2="1" y2="1"><stop offset="0" stop-color="#4f7a2a"/><stop offset=".5" stop-color="#7d9a55"/><stop offset="1" stop-color="#3c5e22"/></linearGradient></defs><rect width="289" height="318" fill="url(#c1)"/></svg>
    <h1 class="cover__title"><span class="light">LET’S </span><span class="bold">CONNECT!</span></h1>
    <p class="cover__tagline">we connect with three best interpreter for your needs and situation, give you confidence that our staff will be there for you</p>
    <p class="cover__name">orvan.llc</p>
  </article>
</section>

<!-- Inside spread -->
<section class="sheet sheet--inside">
  <article class="panel services">
    <h2 class="heading">Our Services</h2>
    <p class="body">Orvan Sign Language Interpreters is the Denver Metro area's premier interpreting agency. We have been providing qualified professional Sign Language Interpreting services since 2008. Our interpreters are carefully screened and handpicked to ensure that your communication needs are met with ease and comfort. We offer superior service at competitive prices with excellent customer service.</p>
    <p class="body strong">Although we specialize in Medical and Educational Interpreting, we also provide services for:</p>
    <div class="service-card">
      <svg class="photo" viewBox="0 0 270 94" preserveAspectRatio="none" role="img" aria-label="Photo of students studying together"><defs><linearGradient id="s1" x1="0" y1="0" x2="1" y2="0"><stop offset="0" stop-color="#c9b8a6"/><stop offset="1" stop-color="#6d7f8e"/></linearGradient></defs><rect width="270" height="94" fill="url(#s1)"/></svg>
      <div class="service-card__label">Educational</div>
    </div>
    <ul class="bullets">
      <li>K-12 Settings</li><li>IEP Meetings</li>
      <li>Post-Secondary</li><li>Staff Meetings</li>
      <li>Parent/Teacher Conference</li><li>Extracurricular Activities</li>
    </ul>
    <div class="service-card">
      <svg class="photo" viewBox="0 0 270 94" preserveAspectRatio="none" role="img" aria-label="Photo of a doctor with a patient"><defs><linearGradient id="s2" x1="0" y1="0" x2="1" y2="0"><stop offset="0" stop-color="#9fb3c6"/><stop offset="1" stop-color="#e8eef3"/></linearGradient></defs><rect width="270" height="94" fill="url(#s2)"/></svg>
      <div class="service-card__label">Medical</div>
    </div>
    <ul class="bullets">
      <li>Doctor's Appointments</li><li>Doctor's Appointments</li>
      <li>ER Visits</li><li>ER Visits</li>
      <li>Patient Education and Counseling</li><li>Patient Education and Counseling</li>
    </ul>
  </article>

  <article class="panel panel--purple settings">
    <div class="service-card">
      <svg class="photo" viewBox="0 0 275 104" preserveAspectRatio="none" role="img" aria-label="Photo of a laptop on a desk at a business meeting"><defs><linearGradient id="s3" x1="0" y1="0" x2="1" y2="1"><stop offset="0" stop-color="#e4e4e2"/><stop offset="1" stop-color="#8e8e8a"/></linearGradient></defs><rect width="275" height="104" fill="url(#s3)"/></svg>
      <div class="service-card__label">Business</div>
    </div>
    <ul class="bullets">
      <li>Staff Meetings</li><li>Conferences</li>
      <li>Interviews &amp; Orientations</li><li>Job Training</li>
    </ul>
    <div class="service-card">
      <svg class="photo" viewBox="0 0 275 104" preserveAspectRatio="none" role="img" aria-label="Photo of a couple exchanging rings at a wedding"><defs><linearGradient id="s4" x1="0" y1="0" x2="1" y2="0"><stop offset="0" stop-color="#2f3542"/><stop offset=".6" stop-color="#d9d6d0"/><stop offset="1" stop-color="#f4f2ee"/></linearGradient></defs><rect width="275" height="104" fill="url(#s4)"/></svg>
      <div class="service-card__label">Special Occasions</div>
    </div>
    <ul class="bullets" style="grid-template-columns:1fr 1fr 1fr">
      <li>Weddings</li><li>Funerals</li><li>Graduations</li>
    </ul>
    <div class="service-card">
      <svg class="photo" viewBox="0 0 275 104" preserveAspectRatio="none" role="img" aria-label="Photo of a white church under a blue sky"><defs><linearGradient id="s5" x1="0" y1="0" x2="0" y2="1"><stop offset="0" stop-color="#3f7fc4"/><stop offset=".6" stop-color="#cfd8e2"/><stop offset="1" stop-color="#6f8a48"/></linearGradient></defs><rect width="275" height="104" fill="url(#s5)"/></svg>
      <div class="service-card__label">Religious</div>
    </div>
    <ul class="bullets">
      <li>Church Services &amp; Sermons</li><li>Religious Ceremonies</li>
      <li>Counseling</li>
    </ul>
    <p class="footer">ORVAN / TDKU, LLC &nbsp;|&nbsp; VOICE : (555) 214-0187 |<br>TEXT : (555) 308-4421 &nbsp;| PO BOX 480312 |<br>DENVER, CO 80222</p>
  </article>

  <article class="panel resources">
    <h2 class="heading">Resources</h2>
    <div class="qa"><div class="qa__marks">Q.<span>A.</span></div><div><p class="qa__q">When do I need to request an interpreter?</p><p class="body">Sign language interpreters are needed when you communicate with a deaf individual whose primary source of communication is sign language. Always ask the deaf person first if an interpreter is needed. A deaf person who is competent in English when writing, reading and speaking may still want an interpreter for more complex or technical situations to ensure effective communication. Lip reading for some deaf people is taxing and is not a reliable means of understanding a conversation in its entirety.</p></div></div>
    <div class="qa"><div class="qa__marks">Q.<span>A.</span></div><div><p class="qa__q">Rights of deaf and hard of hearing/ADA</p><p class="body">The Americans with Disability Act (ADA) is a law that prohibits discrimination against people with disabilities including deaf and hard of hearing individuals. All businesses and government agencies are required to provide effective communication. Please visit www.accessrules.org for more information.</p></div></div>
    <div class="qa"><div class="qa__marks">Q.<span>A.</span></div><div><p class="qa__q">Benefits to small businesses</p><p class="body">Small businesses may qualify for a tax credit under Section 44 of the Internal Revenue Code. This tax incentive was created in 1990 to help small businesses cover ADA related expenses. For more information please visit www.taxhelp.org</p></div></div>
    <h2 class="heading heading--faq">FAQ’s</h2>
    <div class="qa"><div class="qa__marks">Q.<span>A.</span></div><div><p class="qa__q">Can the deaf person bring in their own interpreter?</p><p class="body">It is not recommended. Professional interpreters are trained and must abide by NIA's professional Code of Conduct. This will ensure message accuracy, impartiality and confidentiality.</p></div></div>
    <div class="qa"><div class="qa__marks">Q.<span>A.</span></div><div><p class="qa__q">Is there always a two hour minimum?</p><p class="body">Many assignments require a two hour minimum however we are more than happy to come up with an agreement that fits your needs.</p></div></div>
    <div class="qa"><div class="qa__marks">Q.<span>A.</span></div><div><p class="qa__q">Do you only supply educational interpreters?</p><p class="body">Although our main focus is educational interpreting, we do provide services for medical and community interpreting as well.</p></div></div>
  </article>
</section>

</body>
</html>
```